Labels for Transparent Egg Packs

We want to design a totally new label design concepts for my transparent egg packs , and I want the design in two sepearte sizes / dimensions.
We want it different from what we already have in the market , also using a diffrent color scheme. We want it bright and colorful , not crowded
• Label size 1 : 185*110mm
• Label size 2 : 70*190mm

Target Market(s)

Supermarkets and Retails outlets

Industry/Entity Type

Food

Colors
FFC000
F8CF3A
FAE287
FDF2CF
FEFAEE
F0912C
F2A743
F7CA91
FBE8D2
FDF5EE
EE7325
F08F49
F5BC92
FAE3D3
FDF4ED

Requirements
Must have
• See attached must haves , Must haves contents/ words in design: • Egg quantity: i.e.. 25 grade AA eggs, 30 grade AA eggs • Net weight • Fresh • Natural source of omega-3 • Contact information: __________________________________ Produced and Packaged by Tallowmere Farms Nigeria Address: 12b Okonrin lane , GRA , Ikeja ,Lagos, Nigeria Phone/ Whatsapp : +234 8017443265 , url:www. tallmo.food , Email : info@tallmo.food • Storage Condition : Store in a cool and dry Place • Recycle symbol: • QTLRBE REG: • BKU stamp : • Barcode:
Nice to have
• See attached must haves
Should not have
• No need for Nutritional facts table

```html
<!DOCTYPE html>
<html lang="en">
<head>
<meta charset="utf-8">
<title>Tallmo Farm Fresh Eggs – Pack Label</title>
<link rel="stylesheet" href="https://fonts.googleapis.com/css2?family=Alfa+Slab+One&family=Pacifico&family=PT+Serif:wght@400&display=swap">
<style>
  :root {
    --page: #ffffff;
    --cream: #fdf2cf;
    --cream-light: #fefaee;
    --body-cream: #fdeecd;
    --orange: #f4a30a;
    --orange-deep: #f0912c;
    --yellow: #f9c21e;
    --green: #8bc34a;
    --red: #e32322;
    --red-deep: #b8261f;
    --ink: #1d1d1b;
    --gold: #ffd21f;
    --recycle: #1f8a3a;
  }
  * { box-sizing: border-box; margin: 0; padding: 0; }
  html, body {
    width: 1200px; height: 1200px; overflow: hidden;
    background: var(--page);
  }
  .label {
    position: absolute; left: 57px; top: 338px;
    width: 911px; height: 523px; overflow: hidden;
  }
  .brand-strip {
    position: absolute; left: 0; top: 0; width: 121px; height: 523px;
    background: linear-gradient(90deg, #f6d98a 0%, var(--cream-light) 60%, var(--cream-light) 100%);
  }
  .brand-name {
    position: absolute; left: 56px; top: 282px;
    transform: translate(-50%, -50%) rotate(-90deg);
    font-family: "Alfa Slab One", serif;
    font-size: 52px; line-height: 1; color: var(--ink); white-space: nowrap;
    display: flex; align-items: center; gap: 12px;
  }
  .brand-dot {
    width: 14px; height: 14px; border-radius: 50%; background: var(--green);
  }
  .headline-panel {
    position: absolute; left: 121px; top: 0; width: 349px; height: 425px;
    background: var(--orange);
  }
  .grade-band {
    position: absolute; left: 121px; top: 425px; width: 349px; height: 98px;
    background: var(--green);
    font-family: "Alfa Slab One", serif; color: var(--ink); text-align: center;
  }
  .grade-band .grade { position: absolute; left: 0; right: 0; top: 22px; font-size: 23px; line-height: 30px; }
  .grade-band .weight { position: absolute; left: 0; right: 0; top: 56px; font-size: 17px; line-height: 24px; }
  .farm-fresh {
    position: absolute; left: 121px; width: 349px; top: 32px;
    text-align: center; font-family: "Alfa Slab One", serif; font-weight: 400;
    font-size: 44px; line-height: 48px; color: #fff;
    text-shadow: 3px 3px 0 var(--red-deep);
  }
  .eggs-word {
    position: absolute; left: 121px; width: 349px; top: 108px;
    text-align: center; font-family: "Pacifico", cursive;
    font-size: 100px; line-height: 150px; color: #fff;
    text-shadow: 4px 4px 0 var(--red-deep);
  }
  .count-badge {
    position: absolute; left: 217px; top: 310px; width: 110px; height: 132px;
    border-radius: 50%; background: var(--ink);
    display: flex; align-items: center; justify-content: center;
    font-family: "Alfa Slab One", serif; font-size: 56px; color: var(--gold);
  }
  .hero-art {
    position: absolute; left: 470px; top: 0; width: 441px; height: 523px;
    background: linear-gradient(90deg, var(--yellow) 0%, #fbd04a 70%, var(--orange-deep) 100%);
  }
  .hen-art {
    position: absolute; left: 500px; top: 30px; width: 370px; height: 493px;
    border-radius: 185px 185px 0 0;
    background: linear-gradient(180deg, var(--red) 0%, #ef6a45 30%, var(--body-cream) 62%, var(--body-cream) 100%);
  }
  .omega-claim { position: absolute; left: 0; top: 0; width: 911px; height: 523px; overflow: visible; }
  .omega-claim text {
    font-family: "Alfa Slab One", serif; font-size: 15px; fill: var(--red);
  }
  .info-panel {
    position: absolute; left: 978px; top: 338px; width: 164px; height: 523px;
    background: var(--cream); border-radius: 10px;
  }
  .info-panel text { font-family: "PT Serif", serif; font-size: 9.4px; fill: var(--ink); }
  .info-panel .barcode-caption { font-size: 9px; }
</style>
</head>
<body>
  <section class="label">
    <div class="brand-strip">
      <div class="brand-name"><span class="brand-dot"></span>tallmo</div>
    </div>
    <div class="headline-panel"></div>
    <div class="hero-art"></div>
    <div class="hen-art" role="img" aria-label="Illustration of a white hen with a red comb and wattle, seen in profile"></div>
    <h1 class="farm-fresh">Farm<br>Fresh</h1>
    <div class="eggs-word">Eggs</div>
    <div class="count-badge">25</div>
    <div class="grade-band">
      <p class="grade">Grade AA Eggs</p>
      <p class="weight">Net. Weight 1.5kg</p>
    </div>
    <svg class="omega-claim" viewBox="0 0 911 523">
      <defs>
        <path id="omega-arc" d="M 372 362 A 88 88 0 0 1 545 312"/>
      </defs>
      <circle cx="452" cy="323" r="68" fill="#fdf2cf" role="img" aria-label="Illustration of a fried egg"/>
      <text><textPath href="#omega-arc">A Natural Source of Omega 3</textPath></text>
    </svg>
  </section>

  <aside class="info-panel">
    <svg width="164" height="523" viewBox="0 0 164 523">
      <g class="contact-lines">
        <text transform="translate(24 336) rotate(-90)">Produced and Packaged by Tallowmere Farms Nigeria</text>
        <text transform="translate(36 336) rotate(-90)">12b Okonrin lane , GRA , Ikeja , Lagos, Nigeria</text>
        <text transform="translate(47 336) rotate(-90)">Tel. / WhatsApp : +234 8017443265</text>
        <text transform="translate(59 336) rotate(-90)">www.tallmo.food  •  info@tallmo.food</text>
        <text transform="translate(70 336) rotate(-90)">Store in a cool and dry Place</text>
      </g>
      <g class="recycle-icon" fill="none" stroke="var(--recycle)" stroke-width="6" stroke-linecap="round">
        <path d="M 100 230 A 18 18 0 0 1 120 205"/>
        <path d="M 128 208 A 18 18 0 0 1 132 234"/>
        <path d="M 124 240 A 18 18 0 0 1 102 236"/>
        <path d="M 116 199 L 122 205 L 114 210" stroke-width="4"/>
        <path d="M 138 230 L 132 236 L 127 229" stroke-width="4"/>
        <path d="M 104 243 L 101 235 L 109 232" stroke-width="4"/>
      </g>
      <text transform="translate(150 253) rotate(-90)">Please Recycle</text>
      <circle class="standards-badge" cx="117" cy="300" r="29" fill="#fff" stroke="var(--recycle)" stroke-width="3"/>
      <rect class="barcode-frame" x="10" y="354" width="140" height="90" fill="none" stroke="var(--ink)" stroke-width="1"/>
      <text class="barcode-caption" transform="translate(80 396) rotate(180)" text-anchor="middle">Barcode</text>
    </svg>
  </aside>
</body>
</html>
```